Additional Benefits of Working for VALMIRA

Please prepare an infographic on the additional benefits besides salary of working at VALMIRA as detailed in the attached word document. Also attached is our logo in eps and our company design "Ripples". We are a Not For Profit company that finds jobs for unemployed people of government benefit payments

Arrowmart Market(s)

Attracting people to work for VALMIRA. Making VALMIRA an employer of choice.

Font styles to use
Sans Serif

Colors

Designer to choose colors to be used in the design.

Requirements
Must have
• be on 1 page
• have our logo
Nice to have
• Our Ripples design worked into it.
• Happy engaged employees
• Community engagement - we are a not for profit organisation
Should not have
• Discrimination, swearing,

```html
<!DOCTYPE html>
<html lang="en">
<head>
<meta charset="utf-8">
<title>The Benefits of Working with Us – VALMIRA</title>
<link href="https://fonts.googleapis.com/css2?family=Arimo:wght@400;700&family=Roboto+Condensed:wght@400;500&display=swap" rel="stylesheet">
<style>
  :root{
    --ink:#111;
    --text:#2b2b2b;
    --rule:#9a9a9a;
    --stripe:#ececec;
    --brand:#1d1d1b;
    --brand-green:#5bb531;
    --balance:#6c7274;
    --wellbeing:#f2877c;
    --career:#b39a80;
    --pay:#1fb5c3;
    --perks:#8e3e87;
    --community:#1aaed0;
    --recognition:#e0144f;
    --diversity:#f7b52b;
    --icon-grey:#5f6a6e;
  }
  *{box-sizing:border-box;margin:0;padding:0}
  html,body{width:1200px;height:927px;overflow:hidden;background:#fff}
  body{position:relative;font-family:"Roboto Condensed",Arial,sans-serif;color:var(--text)}
  .stripes{position:absolute;left:0;top:128px;width:1200px;height:758px;
    background:repeating-linear-gradient(-45deg,#fff 0 7px,var(--stripe) 7px 8px)}
  .title{position:absolute;left:54px;top:56px;font-family:"Arimo",Arial,sans-serif;font-weight:700;font-size:52px;letter-spacing:-.3px;color:var(--ink)}
  .brand{position:absolute;left:1022px;top:66px;display:flex;align-items:center;gap:7px;
    font-family:"Arimo",Arial,sans-serif;font-weight:700;font-size:32px;color:var(--brand);letter-spacing:-1px}
  .brand .dot{width:14px;height:14px;border-radius:50%;background:var(--brand-green)}
  .card{position:absolute;width:202px;height:166px;border:2px solid var(--c);border-radius:20px;background:#fff}
  .card svg,.card .placeholder{position:absolute;left:50%;transform:translateX(-50%)}
  .card .label{position:absolute;left:0;right:0;bottom:8px;text-align:center;font-family:"Arimo",Arial,sans-serif;font-weight:700;font-size:15px;line-height:18px;color:var(--ink)}
  .card .label.narrow{font-family:"Roboto Condensed",Arial,sans-serif;font-weight:500;font-size:15.5px}
  .card .link{position:absolute;right:-7px;top:89px;width:12px;height:12px;border-radius:50%;background:var(--c)}
  .row-top{top:162px}
  .row-bottom{top:640px}
  .list{position:absolute;top:343px;width:210px;list-style:none;font-size:14px;line-height:21.5px}
  .list li{position:relative;padding-left:29px;margin-bottom:7px}
  .list li::before{content:"";position:absolute;left:8px;top:10px;width:3px;height:3px;border-radius:50%;background:#333}
  .divider{position:absolute;top:340px;width:1.5px;height:278px;background:linear-gradient(var(--rule) 85%,rgba(154,154,154,0))}
  .caption{position:absolute;top:824px;width:202px;text-align:center;font-size:14px;line-height:21.5px}
  .ripples{position:absolute;left:0;top:886px;width:1200px;height:41px;
    background:linear-gradient(90deg,#2f6a57 0%,#3f4c52 30%,#a8803a 60%,#2f6a57 85%,#4aa374 100%)}
</style>
</head>
<body>
  <div class="stripes"></div>
  <h1 class="title">The Benefits of Working with Us</h1>
  <div class="brand"><span>valmira</span><span class="dot"></span></div>

  <!-- Top row -->
  <div class="card row-top" style="left:54px;--c:var(--balance)">
    <svg width="120" height="110" viewBox="0 0 120 110" style="top:18px">
      <line x1="60" y1="10" x2="60" y2="96" stroke="var(--icon-grey)" stroke-width="5"/>
      <path d="M18 30 Q60 14 102 30" fill="none" stroke="var(--icon-grey)" stroke-width="4"/>
      <rect x="40" y="96" width="40" height="6" rx="2" fill="var(--icon-grey)"/>
      <line x1="18" y1="30" x2="6" y2="70" stroke="var(--icon-grey)" stroke-width="1.5"/>
      <line x1="18" y1="30" x2="30" y2="70" stroke="var(--icon-grey)" stroke-width="1.5"/>
      <line x1="102" y1="30" x2="90" y2="70" stroke="var(--icon-grey)" stroke-width="1.5"/>
      <line x1="102" y1="30" x2="114" y2="70" stroke="var(--icon-grey)" stroke-width="1.5"/>
      <path d="M2 70 H34 Q18 84 2 70Z" fill="var(--icon-grey)"/>
      <path d="M86 70 H118 Q102 84 86 70Z" fill="var(--icon-grey)"/>
      <rect x="9" y="56" width="18" height="12" rx="2" fill="#2a8fd0"/>
      <path d="M102 68 l-7-7 a4 4 0 0 1 7-4 a4 4 0 0 1 7 4z" fill="#e11d2e"/>
    </svg>
    <div class="label">Life Balance</div><div class="link"></div>
  </div>

  <div class="card row-top" style="left:277px;--c:var(--wellbeing)">
    <svg width="120" height="80" viewBox="0 0 120 80" style="top:38px">
      <g fill="var(--wellbeing)">
        <path d="M60 4 C72 24 72 50 60 72 C48 50 48 24 60 4Z"/>
        <path d="M30 18 C48 28 58 52 58 72 C38 64 28 42 30 18Z"/>
        <path d="M90 18 C72 28 62 52 62 72 C82 64 92 42 90 18Z"/>
        <path d="M4 36 C26 40 50 58 56 74 C30 74 12 58 4 36Z"/>
        <path d="M116 36 C94 40 70 58 64 74 C90 74 108 58 116 36Z"/>
      </g>
    </svg>
    <div class="label">Wellbeing</div><div class="link"></div>
  </div>

  <div class="card row-top" style="left:499px;--c:var(--career)">
    <div class="placeholder" role="img" aria-label="Icon of a person climbing rising bar steps" style="top:18px;width:64px;height:92px;border-radius:6px;background:linear-gradient(#5f6a6e 55%,#b39a80 55%)"></div>
    <div class="label narrow">Career Growth &amp;<br>Professional Development</div><div class="link"></div>
  </div>

  <div class="card row-top" style="left:722px;--c:var(--pay)">
    <svg width="110" height="90" viewBox="0 0 110 90" style="top:26px">
      <rect x="38" y="2" width="34" height="14" rx="4" fill="none" stroke="var(--icon-grey)" stroke-width="5"/>
      <rect x="4" y="14" width="94" height="64" rx="6" fill="var(--icon-grey)"/>
      <circle cx="80" cy="62" r="24" fill="#fff"/>
      <circle cx="80" cy="62" r="19" fill="none" stroke="var(--pay)" stroke-width="4"/>
      <text x="80" y="71" text-anchor="middle" font-family="Arimo,Arial,sans-serif" font-weight="700" font-size="24" fill="var(--pay)">$</text>
    </svg>
    <div class="label">Remuneration &amp;<br>Salary Packaging</div><div class="link"></div>
  </div>

  <div class="card row-top" style="left:944px;--c:var(--perks)">
    <svg width="120" height="90" viewBox="0 0 120 90" style="top:28px">
      <rect x="14" y="12" width="102" height="70" rx="5" fill="var(--perks)"/>
      <rect x="36" y="58" width="12" height="4" fill="#fff"/><rect x="54" y="58" width="12" height="4" fill="#fff"/>
      <rect x="72" y="58" width="12" height="4" fill="#fff"/><rect x="90" y="58" width="12" height="4" fill="#fff"/>
      <circle cx="28" cy="26" r="24" fill="#fff"/>
      <circle cx="28" cy="26" r="19" fill="none" stroke="var(--perks)" stroke-width="5"/>
      <path d="M18 26 l7 7 l13-14" fill="none" stroke="var(--perks)" stroke-width="5"/>
    </svg>
    <div class="label">Benefits</div>
  </div>

  <!-- Lists -->
  <ul class="list" style="left:54px">
    <li>VALMIRA Day Leave.<br>An extra day off at Christmas!</li>
    <li>Birthday Leave. A paid day off on your birthday</li>
    <li>A day off every month as Time In Lieu</li>
    <li>4 weeks Annual Leave</li>
    <li>Generous Personal Leave</li>
    <li>Support for parental leave for the birth or adoption of a child</li>
    <li>Flexible work arrangements</li>
  </ul>
  <div class="divider" style="left:274px"></div>
  <ul class="list" style="left:275px">
    <li>Up to $450 per year to spend on Wellbeing services such as gym or yoga memberships</li>
    <li>Free counselling services 24x7 via our Employee Assistance Program</li>
    <li>Discount private health insurance</li>
    <li>WHS policies which support a safe, inclusive work place</li>
  </ul>
  <div class="divider" style="left:491px"></div>
  <ul class="list" style="left:496px">
    <li>Ongoing internal training and development opportunities.</li>
    <li>External study support &amp; study leave</li>
    <li>Access to the tools and technology to do your job well</li>
    <li>Career advancement opportunities</li>
    <li>Internal job vacancy listings</li>
  </ul>
  <div class="divider" style="left:709px"></div>
  <ul class="list" style="left:718px">
    <li>Competitive salary</li>
    <li>Ability to salary package up to $15,900 and reduce your tax. Package rent, home loans, child care and much more</li>
    <li>Salary package up to $2,650 on meal entertainment and holiday accommodation</li>
  </ul>
  <div class="divider" style="left:926px"></div>
  <ul class="list" style="left:938px;width:216px">
    <li>Discounted vouches for Corvo, Fairfield's, Volt HiFi, Lumen, Cask &amp; Co's, ShopLine, Arrowmart, TBG and many others via Benefo e-wallet</li>
    <li>A range of other employee discounts are also available, including access to discounted banking and finance, vehicle purchasing, leasing and hotel accommodation</li>
  </ul>

  <!-- Bottom row -->
  <div class="card row-bottom" style="left:277px;--c:var(--community)">
    <svg width="110" height="90" viewBox="0 0 110 90" style="top:24px">
      <g fill="var(--community)">
        <rect x="32" y="0" width="64" height="16" rx="3"/>
        <rect x="32" y="20" width="64" height="16" rx="3"/>
        <rect x="32" y="40" width="64" height="16" rx="3"/>
        <rect x="6" y="46" width="14" height="40" rx="2"/>
        <path d="M24 50 H52 Q60 50 60 58 H40 M24 50 V84 H70 L104 62 Q100 54 90 58 L72 68 H44"/>
      </g>
    </svg>
    <div class="label narrow">Contributing to Community</div><div class="link"></div>
  </div>

  <div class="card row-bottom" style="left:499px;--c:var(--recognition)">
    <svg width="90" height="96" viewBox="0 0 90 96" style="top:28px">
      <path d="M26 50 L8 84 L22 82 L28 94 L44 62Z M64 50 L82 84 L68 82 L62 94 L46 62Z" fill="var(--recognition)"/>
      <circle cx="45" cy="36" r="32" fill="var(--recognition)"/>
      <circle cx="45" cy="36" r="21" fill="#fff"/>
      <path d="M45 22 l4.2 9 9.8 1.1-7.3 6.6 2 9.7-8.7-5-8.7 5 2-9.7-7.3-6.6 9.8-1.1z" fill="var(--recognition)"/>
    </svg>
    <div class="label">Recognition</div><div class="link"></div>
  </div>

  <div class="card row-bottom" style="left:722px;--c:var(--diversity)">
    <svg width="110" height="90" viewBox="0 0 110 90" style="top:24px">
      <g fill="var(--diversity)">
        <path d="M46 4 A42 42 0 0 0 46 88 L46 64 A18 18 0 0 1 46 28Z"/>
        <path d="M50 4 A42 42 0 0 1 82 18 L64 32 A18 18 0 0 0 50 28Z"/>
        <path d="M86 22 A42 42 0 0 1 100 52 L72 50 A18 18 0 0 0 68 36Z"/>
        <path d="M100 58 A42 42 0 0 1 52 88 L52 64 A18 18 0 0 0 70 56Z"/>
      </g>
    </svg>
    <div class="label">Diversity &amp; Inclusion</div>
  </div>

  <p class="caption" style="left:277px">Team involvement in local charity and community events</p>
  <p class="caption" style="left:499px">We celebrate our people for reaching service milestones</p>
  <p class="caption" style="left:722px">An inclusive and diverse culture where different backgrounds,</p>

  <div class="ripples" role="img" aria-label="Ripples company artwork band in green, slate and ochre tones"></div>
</body>
</html>
```